New Wedding Decor Web Design Project - GUARANTEED PAYMENT

We need to have a business website for a brand new wedding decor & events company, Lirovelle. We have just established our logo and would love to use this logo on the website.

Because this is a new business venture, we do not have too many pictures to post online. It'd be exciting what your creativity can bring us!

Our website is: www.Lirovelle.ca

Target Market(s)

Our clientele demographic is targeted to brides and bridesmaids in their 20-30 years old.

Industry/Entity Type

Wedding

Requirements
Must have
• - Professional, elegant and artistic look
- Modern feeling
- Very catchy flash intro page
- Ability to show Chatterbook posts
Nice to have
• - Easy to navigate, crisp and clean
- Live vocaline messaging or online messaging

I would like to have navigation pages like: Lirovelle Brand, Collections, Features, Contact Us, etc.

Each page I want it to be clean and easy to read. Something like the following website: http://www.pardunetho.com/

We offer:
BACKDROPS
HEAD, CAKE & RECEIVING TABLES DECOR
CHAIRCOVERS
TABLE CLOTHS & OVERLAYS
NAPKINS
CENTREPIECES
CEREMONY SET-UP
CANDELABRA
CRYSTAL GLOBES
LED LIGHTING
CUSTOM DESIGN AISLE RUNNERS
CAKE STANDS
MONEY BOX
CHARGERS
GOBO LIGHTING
Should not have
• - traditional, old style website
- very static (dull)
- too many images or busy layout
- no "standardized" website templates such as: www.brintaq.com/gallery/weddings

```html
<!DOCTYPE html>
<html lang="en">
<head>
<meta charset="utf-8">
<title>Lirovelle</title>
<link rel="stylesheet" href="https://fonts.googleapis.com/css2?family=Questrial&family=Josefin+Sans:wght@300&family=PT+Sans:ital,wght@0,400;0,700;1,400&display=swap">
<style>
:root{
  --green:#6f9a1c;
  --green-band:#a9c65a;
  --green-dark:#5d7f17;
  --text:#4f4f4f;
  --nav:#6a6a6a;
  --pink:#ee6fb1;
  --panel:#f4f4f3;
  --white:#ffffff;
}
*{margin:0;padding:0;box-sizing:border-box}
html,body{width:1200px;height:900px;overflow:hidden}
body{
  position:relative;
  font-family:"PT Sans",sans-serif;color:var(--text);
  background:
    radial-gradient(ellipse 380px 300px at 90px 300px,#f6c7c2 0%,transparent 70%),
    radial-gradient(ellipse 420px 260px at 1150px 230px,#f7d9a0 0%,transparent 70%),
    radial-gradient(ellipse 500px 220px at 600px 20px,#fbe7a6 0%,transparent 75%),
    radial-gradient(ellipse 300px 300px at 1180px 650px,#f1d5d8 0%,transparent 70%),
    #fbf3ee;
}
.header{position:absolute;left:229px;top:22px;width:742px;height:118px;background:var(--white)}
.brand{position:absolute;left:20px;top:42px;display:flex;align-items:center;gap:7px;white-space:nowrap}
.brand-mark{width:24px;height:24px;border-radius:50%;background:#ec5aa7}
.brand-name{font-family:"Questrial",sans-serif;font-size:29px;line-height:34px;color:#7a7a7a}
.header-divider{position:absolute;left:193px;top:16px;width:2px;height:88px;background:#9a9a9a}
.nav{list-style:none}
.nav li{position:absolute;top:74px;font-family:"Questrial",sans-serif;font-size:14.5px;line-height:18px;color:var(--nav);white-space:nowrap}

.tile{position:absolute}
.photo-curtain{background:linear-gradient(160deg,#f2f0f4,#cfc7d6 55%,#e9d6e2)}
.photo-tables{background:linear-gradient(170deg,#e6e2ea,#b7aebf 60%,#f3eef2)}
.photo-hall{background:linear-gradient(180deg,#d9b5d7,#e7d2ea 50%,#cfaed1)}
.photo-lounge{background:linear-gradient(160deg,#d6c6ea,#a89cc4 60%,#e2d9f0)}
.text-tile{background:rgba(246,245,247,.95);padding:14px 10px 0 13px}
.text-tile h2{font-family:"Josefin Sans",sans-serif;font-weight:300;color:var(--green);font-size:25px;line-height:30px;margin-bottom:6px;white-space:nowrap}
.text-tile p{font-size:10px;line-height:16.5px;color:#555;white-space:nowrap}
.text-tile a{display:block;font-size:10px;line-height:16.5px;color:var(--green-dark);text-decoration:none;font-weight:700;white-space:nowrap}

.band{position:absolute;top:539px;height:51px;background:var(--green-band)}
.band h2{font-family:"Josefin Sans",sans-serif;font-weight:300;font-size:32px;line-height:36px;color:#3f4f25;position:absolute;left:18px;top:11px;white-space:nowrap}
.panel{position:absolute;top:590px;height:214px;background:var(--panel);border-bottom:6px solid #d8d8d8}

.fb-head{position:absolute;left:19px;top:24px;display:flex;gap:5px}
.fb-avatar{width:40px;height:40px;background:linear-gradient(135deg,#f3a1c9,#e1549e)}
.fb-name{font-weight:700;font-size:12px;color:#333}
.fb-like{margin-top:5px;display:inline-block;font-size:8px;border:1px solid #aab4cc;background:#eef1f7;color:#3b5a98;padding:2px 4px}
.fb-rule{position:absolute;left:16px;width:250px;height:1px;background:#9eb070}
.fb-count{position:absolute;left:21px;top:77px;font-size:8.5px;color:#333}
.fans{position:absolute;left:21px;top:92px;display:flex;gap:4px}
.fan{width:38px;text-align:center;font-size:7.5px;color:#555;white-space:nowrap}
.fan span{display:block;width:38px;height:38px;margin-bottom:4px;background:linear-gradient(160deg,#9a9a9a,#4d4d4d)}
.fb-foot{position:absolute;left:21px;top:166px;font-size:8px;color:#3b5a98;display:flex;align-items:center;gap:4px}
.fb-foot i{width:10px;height:10px;background:#3b5a98}

.field-label{position:absolute;font-style:italic;font-size:15px;color:var(--green)}
.field{position:absolute;border:1px solid #cfcfcf;border-radius:3px;
  background:repeating-linear-gradient(135deg,#fafafa 0 3px,#ececec 3px 4px)}
.send{position:absolute;left:212px;top:152px;width:184px;height:28px;border-radius:5px;
  background:linear-gradient(#f58ac3,#e9619f);color:#fff;font-family:"Questrial",sans-serif;font-size:16px;
  display:flex;align-items:center;justify-content:center;box-shadow:0 2px 3px rgba(0,0,0,.15)}

.footer{position:absolute;top:811px;left:232px;width:736px;height:18px;font-size:11px;color:#777;display:flex;align-items:center;white-space:nowrap}
.footer-links{margin-left:auto;display:flex;gap:8px;align-items:center}
.social{display:flex;align-items:center;gap:4px;font-size:10px;color:#4a6aa8;margin-left:8px}
.social i{width:10px;height:10px;border-radius:50%;background:#4a6aa8}
.social.alt{color:#1aa7e0}.social.alt i{background:#1aa7e0}
</style>
</head>
<body>
<header class="header">
  <div class="brand"><span class="brand-mark"></span><span class="brand-name">Lirovelle</span></div>
  <div class="header-divider"></div>
  <ul class="nav">
    <li style="left:226px">Home</li>
    <li style="left:305px">Lirovelle Brand</li>
    <li style="left:455px">Collections</li>
    <li style="left:564px">Features</li>
    <li style="left:658px">Contact Us</li>
  </ul>
</header>

<div class="tile photo-curtain" style="left:229px;top:149px;width:193px;height:149px" role="img" aria-label="White and purple draped backdrop with branches"></div>
<div class="tile photo-curtain" style="left:423px;top:149px;width:130px;height:149px" role="img" aria-label="Pink-lit draped backdrop with floral table"></div>
<div class="tile text-tile" style="left:554px;top:149px;width:169px;height:149px">
  <h2>Lorem Ipsum</h2>
  <p>Vivamus et ligula lacus. Ut eu erat<br>nisl. Duis mi ante, iaculis molestie<br>sodales nec, tempus sollicitudin<br>lacus lambert adam.</p>
  <a>- Learn More</a>
</div>
<div class="tile photo-lounge" style="left:724px;top:149px;width:247px;height:149px" role="img" aria-label="Cocktail tables with grey linens under purple lighting"></div>

<div class="tile photo-tables" style="left:229px;top:300px;width:193px;height:231px" role="img" aria-label="Banquet table with grey cloth, pink runner and white chairs"></div>
<div class="tile photo-tables" style="left:423px;top:300px;width:130px;height:125px" role="img" aria-label="Table settings with pink sashes"></div>
<div class="tile text-tile" style="left:423px;top:426px;width:130px;height:105px;padding-top:9px;padding-left:10px">
  <h2 style="margin-bottom:3px">Duis Tepur</h2>
  <p>Vivamus et ligula lacus.<br>Ut eu era nisl.</p>
  <a>- Learn More</a>
</div>
<div class="tile photo-hall" style="left:554px;top:300px;width:253px;height:231px" role="img" aria-label="Reception hall with chandeliers and draped ceiling"></div>
<div class="tile text-tile" style="left:808px;top:300px;width:163px;height:125px;padding-top:13px;padding-left:11px">
  <h2 style="font-size:24px;margin-bottom:3px">Dolor Sit Amet</h2>
  <p>Vivamus et ligula lacus. Ut eu era<br>nisl. Duis mi ante, iaculis molese<br>sodales nec.</p>
  <a>- Learn More</a>
</div>
<div class="tile photo-hall" style="left:808px;top:426px;width:163px;height:105px" role="img" aria-label="Dining room with covered chairs"></div>

<div class="band" style="left:229px;width:323px"><h2>like us</h2></div>
<div class="band" style="left:554px;width:417px"><h2 style="left:16px">contact us</h2></div>

<section class="panel" style="left:229px;width:323px">
  <div class="fb-head">
    <div class="fb-avatar" role="img" aria-label="Page picture of a pink flower"></div>
    <div><div class="fb-name">Lirovelle</div><span class="fb-like">Like</span></div>
  </div>
  <div class="fb-rule" style="top:70px"></div>
  <div class="fb-count">143 people like <b>Lirovelle.</b></div>
  <div class="fans">
    <div class="fan"><span role="img" aria-label="Fan picture"></span>Marisol</div>
    <div class="fan"><span role="img" aria-label="Fan picture"></span>Torben</div>
    <div class="fan"><span role="img" aria-label="Fan picture"></span>Pippet</div>
    <div class="fan"><span role="img" aria-label="Fan picture"></span>R.J. Tamsin</div>
    <div class="fan"><span role="img" aria-label="Fan picture"></span>Osric</div>
    <div class="fan"><span role="img" aria-label="Fan picture"></span>Vianne</div>
  </div>
  <div class="fb-rule" style="top:152px"></div>
  <div class="fb-foot"><i></i>Chatterbook social plugin</div>
</section>

<section class="panel" style="left:554px;width:417px">
  <div class="field-label" style="left:19px;top:20px">Name:</div>
  <div class="field" style="left:15px;top:41px;width:165px;height:28px"></div>
  <div class="field-label" style="left:19px;top:76px">Number:</div>
  <div class="field" style="left:15px;top:97px;width:165px;height:28px"></div>
  <div class="field-label" style="left:19px;top:132px">Email:</div>
  <div class="field" style="left:15px;top:152px;width:165px;height:28px"></div>
  <div class="field-label" style="left:215px;top:20px">Message:</div>
  <div class="field" style="left:210px;top:41px;width:187px;height:96px"></div>
  <div class="send">Send Message</div>
</section>

<footer class="footer">
  <span>© Copyright 2013 Lirovelle</span>
  <nav class="footer-links">
    <span>Lirovelle Brand</span><span>Collections</span><span>Features</span><span>Contact Us</span>
    <span class="social"><i></i>Chatterbook</span>
    <span class="social alt"><i></i>vocaline</span>
  </nav>
</footer>
</body>
</html>
```